BRC Trifold

- Hello -
We are looking for an exciting trifold design for our residential roofing and interior remodeling company. Below is the website for more inspiration and images. We would like to include the Veteran Owned section somewhere on the back.

https://brellmontroofingandconstruction.com/

Thank You,
Wesley

```html
<!DOCTYPE html>
<html lang="en">
<head>
<meta charset="utf-8">
<title>BRC Trifold</title>
<link rel="stylesheet" href="https://fonts.googleapis.com/css2?family=Montserrat:wght@400;500;600;700;800&family=Raleway:wght@400;500;600&display=swap">
<style>
:root{
  --stage:#4b4b4b;
  --maroon:#722f34;
  --stone:#a69a94;
  --stone-panel:#a1958f;
  --white:#ffffff;
  --ink:#55504d;
  --photo-sky:#9fb7a6;
  --photo-green:#6f9a4f;
  --photo-wood:#b08a66;
  --photo-marble:#dcdad6;
}
*{margin:0;padding:0;box-sizing:border-box}
html,body{width:1018px;height:1200px;overflow:hidden;background:var(--stage)}
body{position:relative;font-family:"Raleway",sans-serif;color:var(--ink)}
.abs{position:absolute}
.panel{position:absolute;background:var(--white);overflow:hidden}
.outside{left:159px;top:79px;width:712px;height:504px}
.inside{left:160px;top:620px;width:697px;height:492px}
.shapes{position:absolute;left:0;top:0}

/* outside left */
.perks-title{left:20px;top:204px;width:220px;font-family:"Montserrat",sans-serif;font-weight:700;font-size:16px;line-height:18.5px;color:var(--maroon);white-space:nowrap}
.perks-list{left:29px;top:274px;width:200px;list-style:none;border-left:1px solid var(--maroon)}
.perk{position:relative;padding-left:11px;font-size:8.4px;line-height:11px;color:var(--maroon);font-weight:500;white-space:nowrap}
.perk::before{content:"";position:absolute;left:-5px;top:0.5px;width:10px;height:10px;border-radius:50%;background:var(--maroon)}
.perk::after{content:"";position:absolute;left:-2px;top:3px;width:4px;height:2.5px;border-left:1.5px solid #fff;border-bottom:1.5px solid #fff;transform:rotate(-45deg)}
.perk-gap{height:11px;list-style:none}

/* photo tabs */
.tab{font-family:"Montserrat",sans-serif;font-weight:600;font-size:8px;color:#fff;background:var(--maroon);padding:2px 6px}

/* contact block */
.contact{left:237px;top:318px;width:238px;text-align:center;color:#fff}
.contact-name{font-family:"Montserrat",sans-serif;font-weight:700;font-size:10.6px}
.contact-addr{font-family:"Montserrat",sans-serif;font-size:10.4px;line-height:14px}
.contact-phone{font-family:"Montserrat",sans-serif;font-weight:800;font-size:18px;margin-top:6px;display:flex;justify-content:center;align-items:center;gap:3px}
.contact-mail{font-family:"Montserrat",sans-serif;font-style:italic;font-size:10px;margin-top:1px}
.web-pill{display:inline-block;margin-top:8px;background:#fff;color:#222;border-radius:9px;padding:2px 10px;font-family:"Montserrat",sans-serif;font-weight:600;font-size:10.5px;letter-spacing:1.8px}

/* brand */
.brand{font-family:"Montserrat",sans-serif;color:var(--maroon)}
.brand-name{font-weight:700;font-size:14.5px;letter-spacing:2.2px}
.brand-sub{font-family:"Montserrat",sans-serif;font-size:7.4px;letter-spacing:4.2px;color:var(--stone);white-space:nowrap}
.brand-mark{width:14px;height:14px;background:var(--maroon)}

.about{left:490px;top:305px;width:205px;font-size:8.4px;line-height:10.2px;color:var(--ink)}
.services{top:358px;font-size:8.4px;line-height:11.2px;white-space:nowrap}
.services h3{font-family:"Montserrat",sans-serif;font-weight:800;font-size:11.5px;line-height:11px;color:var(--maroon)}
.services h4{font-family:"Montserrat",sans-serif;font-weight:700;font-size:5.6px;color:var(--maroon);margin-bottom:4px}
.services ul{list-style:none}
.services li{position:relative;padding-left:11px}
.services li::before{content:"";position:absolute;left:0;top:3px;width:6px;height:6px;border:1px solid var(--maroon)}
.services li::after{content:"";position:absolute;left:1.5px;top:3.5px;width:4px;height:2px;border-left:1.2px solid var(--maroon);border-bottom:1.2px solid var(--maroon);transform:rotate(-45deg)}
.services-divider{left:564px;top:360px;width:1px;height:68px;background:var(--maroon)}

.footer-phone{left:504px;top:458px;width:180px;text-align:right;font-family:"Montserrat",sans-serif;font-weight:800;font-size:18.5px;line-height:20px;letter-spacing:3px;color:#fff;white-space:nowrap}
.footer-web{left:502px;top:482px;font-family:"Montserrat",sans-serif;font-weight:500;font-size:12px;line-height:14px;letter-spacing:3.2px;color:#fff;white-space:nowrap}
.social{left:293px;top:472px;display:flex;gap:3px}
.social span{width:16px;height:16px;border-radius:50%;border:2px solid #fff}

/* inside */
.photo{position:absolute}
.band{position:absolute;background:var(--maroon);color:#fff;font-family:"Montserrat",sans-serif;font-weight:700;font-size:12.6px;padding-left:17px;display:flex;align-items:center;white-space:nowrap}
.copy{position:absolute;font-size:9.2px;line-height:11.8px;color:var(--ink);text-align:justify}
.copy b{font-weight:700;color:#333}
.sub-head{font-family:"Raleway",sans-serif;font-weight:600;font-size:11.5px;line-height:13px;white-space:nowrap}
.accent{font-family:"Montserrat",sans-serif;font-weight:600;font-size:11px;color:var(--maroon)}
.stone-panel{position:absolute;background:var(--stone-panel)}
.kitchen-copy{left:246px;top:58px;width:204px;font-size:9.2px;line-height:11.9px;color:#fff}
.quote-box{left:246px;top:349px;width:201px;height:82px;border:1px solid #fff}
.quote-mark{left:325px;top:325px;width:43px;height:43px;border-radius:50%;background:var(--maroon);color:#fff;font-family:"Montserrat",sans-serif;font-weight:800;font-size:44px;line-height:56px;text-align:center}
.quote-text{left:246px;top:370px;width:201px;text-align:center;color:#fff;font-size:10px;line-height:13px;white-space:nowrap}
.quote-author{left:246px;top:424px;width:201px;text-align:center}
.quote-author span{background:var(--stone-panel);padding:0 2px;font-family:"Montserrat",sans-serif;font-weight:700;font-size:10px;color:var(--maroon)}
.quote-web{left:229px;top:456px;width:234px;text-align:center;font-family:"Montserrat",sans-serif;font-size:13px;color:var(--maroon)}
.quote-web b{font-weight:800}
.phone-pill{left:17px;top:455px;width:194px;height:22px;border-radius:11px;background:var(--maroon);color:#fff;font-family:"Montserrat",sans-serif;font-weight:800;font-size:18px;letter-spacing:2px;display:flex;align-items:center;justify-content:center;gap:3px;white-space:nowrap}
</style>
</head>
<body>

<section class="panel outside" aria-label="Trifold outside">
  <svg class="shapes" width="712" height="504" viewBox="0 0 712 504">
    <polygon points="325,0 475,0 475,453 237,453 237,102" fill="var(--maroon)"/>
    <polygon points="0,98 64,0 325,0 164,186 0,186" fill="var(--stone)"/>
    <polygon points="14,150 14,64 70,10 283,10 150,160 20,160" fill="var(--photo-wood)" role="img" aria-label="Photo of a modern kitchen with wood cabinets and pendant lights"/>
    <rect x="267" y="32" width="177" height="117" fill="#fff"/>
    <rect x="269" y="34" width="173" height="113" fill="var(--photo-green)" role="img" aria-label="Before photo of a ranch house with a green lawn"/>
    <rect x="267" y="172" width="177" height="117" fill="#fff"/>
    <rect x="269" y="174" width="173" height="113" fill="var(--photo-sky)" role="img" aria-label="After photo of the renovated white ranch house"/>
    <polygon points="526,90 712,90 712,102 613,291 349,291" fill="var(--stone)"/>
    <polygon points="540,116 657,116 574,264 405,264" fill="var(--photo-sky)" role="img" aria-label="Photo of a white cottage-style home with a new roof"/>
    <polygon points="237,452 672,449 695,416 712,432 712,504 237,504" fill="var(--maroon)"/>
    <polyline points="237,447 670,444 695,411 712,427" fill="none" stroke="var(--stone)" stroke-width="3"/>
  </svg>

  <span class="abs tab" style="left:399px;top:127px">BEFORE</span>
  <span class="abs tab" style="left:270px;top:260px">AFTER</span>

  <h2 class="abs perks-title">PERKS THAT COME<br>FROM WORKING WITH<br>PROFESSIONALS</h2>
  <ul class="abs perks-list">
    <li class="perk">Free Estimate</li>
    <li class="perk-gap"></li>
    <li class="perk">Professional Interior<br>Design Consultation</li>
    <li class="perk-gap"></li>
    <li class="perk">Insurance Inspections assistance<br>for an accurate assessment</li>
    <li class="perk-gap"></li>
    <li class="perk">Insurance claim advocacy</li>
    <li class="perk-gap"></li>
    <li class="perk">Once stop shop – General Contractor<br>to assist with all of your Restoration &amp;<br>Renovation needs</li>
    <li class="perk-gap"></li>
    <li class="perk">Referral Bonus</li>
    <li class="perk-gap"></li>
    <li class="perk">Military Discount</li>
    <li class="perk-gap"></li>
    <li class="perk">Free Architectural Consultation</li>
  </ul>

  <div class="abs contact">
    <div class="contact-name">Brellmont Roofing &amp; Construction</div>
    <div class="contact-addr">4180 Larkspur Avenue, Suite B<br>Fairmont, IL 60999</div>
    <div class="contact-phone">
      <svg width="13" height="13" viewBox="0 0 24 24"><path d="M6.6 10.8a15 15 0 0 0 6.6 6.6l2.2-2.2a1 1 0 0 1 1-.25 11.4 11.4 0 0 0 3.6.57 1 1 0 0 1 1 1V20a1 1 0 0 1-1 1A17 17 0 0 1 3 4a1 1 0 0 1 1-1h3.5a1 1 0 0 1 1 1c0 1.25.2 2.45.57 3.57a1 1 0 0 1-.25 1z" fill="none" stroke="#fff" stroke-width="1.8"/></svg>
      555-014-2870
    </div>
    <div class="contact-mail">brellmontroofing@example.com</div>
    <div class="web-pill">WWW.BRELLMONT.COM</div>
  </div>

  <div class="abs brand" style="left:498px;top:50px;display:flex;align-items:center;gap:6px">
    <span class="brand-mark"></span><span class="brand-name">BRELLMONT</span>
  </div>
  <div class="abs brand-sub" style="left:498px;top:69px">ROOFING &amp; CONSTRUCTION</div>

  <p class="abs about">Licensed &amp; accredited company with over 20 years construction experience in Residential &amp; Commercial Renovation &amp; Restoration.</p>

  <div class="abs services" style="left:489px">
    <h3>EXTERIOR</h3><h4>HOME REMODELING</h4>
    <ul><li>Roofing</li><li>Siding</li><li>Gutters</li><li>Soffit / Fascia</li></ul>
  </div>
  <div class="abs services-divider"></div>
  <div class="abs services" style="left:576px">
    <h3>INTERIOR</h3><h4>HOME REMODELING</h4>
    <ul><li>Home Improvement</li><li>Kitchen Remodeling</li><li>Bathroom Remodeling</li><li>Deck / Patio Build Ou</li></ul>
  </div>

  <div class="abs social" aria-label="Social media links"><span></span><span></span><span></span><span></span><span></span></div>
  <div class="abs footer-phone">555-014-2870</div>
  <div class="abs footer-web">WWW.BRELLMONT.COM</div>
</section>

<section class="panel inside" aria-label="Trifold inside">
  <div class="photo" style="left:0;top:0;width:229px;height:151px;background:linear-gradient(160deg,var(--photo-green),#4b5563)" role="img" aria-label="Aerial photo of a house with a new dark shingle roof"></div>
  <div class="band" style="left:0;top:151px;width:229px;height:33px">ROOFING,SIDING &amp; GUTTER</div>
  <p class="copy" style="left:17px;top:197px;width:199px">Whether you’re looking to do roof repair, roof replacement, new gutters, new siding, trust our licensed professionals. We work with the top manufacturers in the industry <b>Crestline Summit Roofing System</b> – Gale Guard Shake, Ridgeway Pure</p>
  <div class="abs accent" style="left:18px;top:275px">Lifetime Warranty</div>
  <div class="band" style="left:0;top:302px;width:229px;height:33px">STORM DAMAG</div>
  <div class="abs sub-head" style="left:16px;top:346px">Renovation or Restoration</div>
  <p class="copy" style="left:16px;top:359px;width:198px;font-size:8.9px;line-height:11.6px">Time for new Roof, Siding or Gutters? Hail or Storm damage? We are here to assist in every aspect. With decades of experience negotiating with Insurance companies for accurate assessments, we work with the best trades for the project, and ensure your home is not only built well but looks just as beautiful.</p>
  <div class="abs phone-pill">
    <svg width="14" height="14" viewBox="0 0 24 24"><path d="M6.6 10.8a15 15 0 0 0 6.6 6.6l2.2-2.2a1 1 0 0 1 1-.25 11.4 11.4 0 0 0 3.6.57 1 1 0 0 1 1 1V20a1 1 0 0 1-1 1A17 17 0 0 1 3 4a1 1 0 0 1 1-1h3.5a1 1 0 0 1 1 1c0 1.25.2 2.45.57 3.57a1 1 0 0 1-.25 1z" fill="none" stroke="#fff" stroke-width="1.8"/></svg>
    555-014-2870
  </div>

  <div class="stone-panel" style="left:229px;top:0;width:234px;height:492px"></div>
  <div class="band" style="left:229px;top:0;width:234px;height:33px">KITCHEN REMODELING</div>
  <p class="abs kitchen-copy">Your kitchen is the central hub of every home. We’ll collaborate with you to make this space open and functional for everyone to enjoy. We use the latest building products and trends to meet and exceed your expectations.</p>
  <div class="photo" style="left:229px;top:151px;width:234px;height:184px;background:linear-gradient(170deg,#eceae6,#b9b3ac 70%,#8a7a6a)" role="img" aria-label="Photo of a bright white kitchen with a granite island and stainless appliances"></div>
  <div class="abs quote-box"></div>
  <div class="abs quote-mark">“</div>
  <p class="abs quote-text">I wake up every day excited<br>to use my dream kitchen. Thank you,<br>Brellmont Roofing &amp; Construction!</p>
  <div class="abs quote-author"><span>- CARLA BENTON</span></div>
  <div class="abs quote-web">www.<b>BRELLMONT</b>.com</div>

  <div class="photo" style="left:463px;top:0;width:234px;height:151px;background:linear-gradient(135deg,#c9cdcc,var(--photo-marble))" role="img" aria-label="Photo of a marble bathroom with a glass shower and soaking tub"></div>
  <div class="photo" style="left:463px;top:151px;width:234px;height:149px;background:linear-gradient(135deg,#efeeec,#b7aa9c)" role="img" aria-label="Photo of a modern bathroom with a wood vanity and freestanding tub"></div>
  <div class="band" style="left:463px;top:300px;width:234px;height:34px">BATHROOM REMODELING</div>
  <div class="abs sub-head" style="left:480px;top:343px">Make It Picture Perfect</div>
  <p class="copy" style="left:480px;top:356px;width:200px">Give your bathroom a new life and increase the value of your home at the same time. We offer full service design assistance to transform the bathroom into your very own spa retreat.</p>
  <div class="abs brand" style="left:494px;top:448px;display:flex;align-items:center;gap:6px">
    <span class="brand-mark"></span><span class="brand-name">BRELLMONT</span>
  </div>
  <div class="abs brand-sub" style="left:494px;top:467px">ROOFING &amp; CONSTRUCTION</div>
</section>

</body>
</html>
```